Say Something About Privacy!!!

We need a poster designed with the theme of "Privacy". With so many digital assistants (Vonu, Marvo, Plinker, etc) listening to our conversations and web cams watching our activities privacy is becoming more important than ever. The goal of the project is to design a poster that can be used as giveaway item at trade shows, etc. The poster should be engaging and thought provoking. The tone can be serious or lighthearted. You can use a photo, illustration, or just copy to get your point across. I've included a few examples of other posters I like.

Target Market(s)

General Public. Well educated. Tech enthusiasts. People with smartphones and/or smart speakers.

Industry/Entity Type

Cyber Security

Font styles to use
Sans Serif

Requirements
Must have
• Simple design. Strong colours.
Should not have
• While this is a serious subject, I don't want the message to be too threatening.

```html
<!DOCTYPE html>
<html lang="en">
<head>
<meta charset="utf-8">
<title>Privacy Poster</title>
<link rel="stylesheet" href="https://fonts.googleapis.com/css2?family=Crimson+Pro:wght@400;500&family=Open+Sans:wght@400;600&display=swap">
<style>
  :root {
    --red-top: #e3202a;
    --red-mid: #a8141c;
    --dark-bottom: #2a2626;
    --frame: #ffffff;
    --text-light: #ffffff;
    --accent: #ff3a3a;
  }
  html, body {
    margin: 0;
    padding: 0;
    overflow: hidden;
  }
  .poster {
    position: relative;
    width: 831px;
    height: 1200px;
    background: linear-gradient(160deg, var(--red-top) 0%, var(--red-mid) 50%, var(--dark-bottom) 100%);
    overflow: hidden;
    font-family: "Crimson Pro", Georgia, serif;
    color: var(--text-light);
  }
  .poster-frame {
    position: absolute;
    left: 30px;
    top: 30px;
    right: 30px;
    bottom: 30px;
    border: 3px solid var(--frame);
  }
  .headline {
    position: absolute;
    left: 0;
    right: 0;
    top: 205px;
    margin: 0;
    text-align: center;
    font-weight: 400;
    text-transform: uppercase;
    line-height: 0.9;
  }
  .headline span { display: block; }
  .line-know { font-size: 104px; }
  .line-what { font-size: 86px; margin-top: 10px; }
  .line-ate { font-size: 200px; margin-top: 6px; }
  .line-last { font-size: 156px; }
  .line-evening { font-size: 112px; margin-top: 8px; }
  .statement {
    position: absolute;
    left: 228px;
    top: 880px;
    margin: 0;
    font-family: "Open Sans", Arial, sans-serif;
    font-weight: 400;
    font-size: 25px;
    line-height: 1.25;
    text-transform: uppercase;
    letter-spacing: 0.5px;
  }
  .tagline {
    position: absolute;
    left: 228px;
    top: 968px;
    margin: 0;
    font-family: "Open Sans", Arial, sans-serif;
    font-weight: 400;
    font-size: 31px;
    color: var(--accent);
    text-transform: uppercase;
  }
</style>
</head>
<body>
  <main class="poster">
    <div class="poster-frame"></div>
    <h1 class="headline">
      <span class="line-know">I Know</span>
      <span class="line-what">What You</span>
      <span class="line-ate">Ate</span>
      <span class="line-last">Last</span>
      <span class="line-evening">Evening</span>
    </h1>
    <p class="statement">Privacy is a fundamental right of<br>every human being.</p>
    <p class="tagline">Stay aware. Stay safe.</p>
  </main>
</body>
</html>
```